Byte Lantern Website

Design and implement (fully coded and ready to launch) website for a professional services company - please see the documents attached and send us an email if there are any questions
Target Market(s)
Market to potential clients about the services we offer and be able to reach us for any consulting opportunities
Industry/Entity Type
Professional Service
Coding
Coded - Design and coding required
Number of Pages Required
3 page
Requirements
Must have
- Single page website design that is SEO optimized
Blog Post
Contact US page
Cool images/ logos for the service offering - not fill the website with text/content
Must be professional looking website
Coded website should also look great on different screens - mobile, tablets etc
Nice to have
- Choose easy neutral colors that compliment the logo colors. Having said that don't use every color in the logo for the website design.
Should not have
- Too many colors and several various different fonts

```html
<!DOCTYPE html>
<html lang="en">
<head>
<meta charset="utf-8">
<title>Byte Lantern — Website</title>
<link rel="stylesheet" href="https://fonts.googleapis.com/css2?family=Montserrat:wght@300;400;500;600;700&display=swap">
<style>
:root{
  --red:#ee2f3a;
  --magenta:#c4357a;
  --purple:#a7429c;
  --orange:#f58a2a;
  --ink:#151515;
  --text:#555;
  --muted:#8a8a8a;
  --soft:#f5f5f6;
  --line:#e4e4e4;
  --black:#000;
  --bar:#161616;
  --white:#fff;
}
*{box-sizing:border-box;margin:0;padding:0}
html,body{width:1200px;height:4174px;overflow:hidden}
body{background:var(--white);font-family:'Montserrat',sans-serif;color:var(--ink);position:relative}
.a{position:absolute}
.brand{left:0;width:1200px;top:205px;text-align:center;font-weight:600;font-size:62px;letter-spacing:3px;color:var(--ink);line-height:1}
.brand-llc{left:812px;top:276px;font-weight:600;font-size:24px;letter-spacing:2px}
.frame{background:var(--white);overflow:hidden;box-shadow:0 4px 24px rgba(0,0,0,.08)}
.desktop{left:350px;top:382px;width:764px;height:3157px}
.mobile{left:86px;top:382px;width:178px;height:3673px}
.logo-text{font-weight:600;color:var(--ink);letter-spacing:.5px;white-space:nowrap}
.logo-dot{display:inline-block;border-radius:50%;background:var(--magenta);vertical-align:middle}
.nav{font-size:8px;color:#444}
.pill{border-radius:20px;background:var(--purple);color:#fff;text-align:center;font-weight:500}
.hero{background:linear-gradient(180deg,#ef3340 0%,#d8365f 45%,#b9408f 100%);overflow:hidden}
.ring{border-radius:50%;background:rgba(255,255,255,.06)}
.center{text-align:center}
.white{color:#fff}
.light{font-weight:300}
.bold{font-weight:700}
.semi{font-weight:600}
.btn-outline{border:1px solid rgba(255,255,255,.85);border-radius:20px;color:#fff;text-align:center}
.btn-red{background:var(--red);border-radius:20px;color:#fff;text-align:center;font-weight:500}
.btn-white{background:#fff;border-radius:20px;color:var(--purple);text-align:center;font-weight:500}
.partner{background:#e7e7ea;border-radius:6px}
.divider{background:var(--line);width:1px}
.circle-btn{border-radius:50%;background:#fff;box-shadow:0 1px 6px rgba(0,0,0,.15);display:flex;align-items:center;justify-content:center}
.photo-about{background:radial-gradient(circle at 45% 40%,#f4e6dc 0%,#c9a993 35%,#7d6d6a 70%,#b7b2b4 100%);border-radius:0 0 120px 0}
.kicker{color:var(--muted);font-weight:400}
.h2{font-weight:600;color:var(--ink);line-height:1.2}
.p{color:var(--text);line-height:1.7}
.svc-icon{border-radius:50%;background:#fff;box-shadow:0 2px 8px rgba(0,0,0,.1);display:flex;align-items:center;justify-content:center}
.svc-icon.fill{background:var(--purple)}
.svc-title{font-weight:500;color:var(--ink)}
.portrait{border-radius:50%;background:radial-gradient(circle at 50% 40%,#c9b3a3 0%,#8a6f60 40%,#4d4a4c 75%,#d8d8d8 100%)}
.faint-ring{border-radius:50%;border:14px solid rgba(238,47,58,.07)}
.social{border-radius:50%;background:#2b93d6;display:flex;align-items:center;justify-content:center}
.cta{background:var(--purple)}
.card{background:#fff;box-shadow:0 4px 16px rgba(0,0,0,.08);overflow:hidden}
.card-img{background:linear-gradient(160deg,#2b4d7a 0%,#7aa1c7 40%,#d9e4ef 70%,#1f3656 100%)}
.card-img.desk{background:linear-gradient(160deg,#e9e9ea 0%,#b6b9bf 40%,#5a5f66 70%,#dcdcdc 100%)}
.footer{background:var(--black)}
.footer-bar{background:var(--bar)}
.f-head{color:#fff;font-weight:400}
.f-link{color:#cfcfcf}
.f-field{color:#6d6d6d;border-bottom:1px solid #3a3a3a}
.s-dot{border-radius:50%;background:#3b6fd1}
</style>
</head>
<body>

<!-- Brand wordmark -->
<div class="a brand">BYTE LANTERN</div>
<div class="a brand-llc">LLC</div>

<!-- ================= DESKTOP ================= -->
<section class="a frame desktop" aria-label="Desktop layout">
  <!-- header -->
  <div class="a logo-text" style="left:47px;top:14px;font-size:11px"><span class="logo-dot" style="width:9px;height:9px;margin-right:5px"></span>BYTE LANTERN</div>
  <div class="a nav" style="left:439px;top:20px">Home</div>
  <div class="a nav" style="left:479px;top:20px">Our Services</div>
  <div class="a nav" style="left:545px;top:20px">About Us</div>
  <div class="a nav" style="left:599px;top:20px">Blogs</div>
  <div class="a pill" style="left:649px;top:15px;width:68px;height:22px;font-size:8px;line-height:22px">Contact Us</div>

  <!-- hero -->
  <div class="a hero" style="left:0;top:50px;width:764px;height:424px">
    <div class="a ring" style="left:-160px;top:-200px;width:560px;height:560px"></div>
    <div class="a ring" style="left:330px;top:40px;width:620px;height:620px"></div>
    <div class="a ring" style="left:560px;top:-220px;width:380px;height:380px"></div>
    <div class="a center white light" style="left:0;width:764px;top:122px;font-size:20px">Let's Put Your</div>
    <div class="a" style="left:152px;top:168px;width:73px;height:2px;background:var(--orange)"></div>
    <div class="a center white semi" style="left:0;width:764px;top:143px;font-size:40px">Data To Work</div>
    <div class="a center white" style="left:150px;width:464px;top:209px;font-size:7.5px;line-height:13px">Lorem Ipsum Is Simply Dummy Text Of The Printing And Typesetting Industry. Lorem Ipsum Has Been The Industry's Standard Dummy Text Ever Since The 1500s, When An Unknown Printer Took A Galley Of Type And Scrambled It To Make A Type Specimen Book.</div>
    <div class="a btn-outline" style="left:347px;top:279px;width:71px;height:22px;font-size:8px;line-height:20px">Get Started</div>
  </div>

  <!-- partners -->
  <div class="a circle-btn" style="left:51px;top:558px;width:24px;height:24px"><svg width="10" height="8" viewBox="0 0 10 8"><path d="M9 4H1M4 1L1 4l3 3" stroke="#333" fill="none" stroke-width="1"/></svg></div>
  <div class="a partner" style="left:110px;top:560px;width:86px;height:20px" role="img" aria-label="Partner badge"></div>
  <div class="a divider" style="left:225px;top:552px;height:36px"></div>
  <div class="a partner" style="left:270px;top:558px;width:54px;height:24px" role="img" aria-label="Partner badge"></div>
  <div class="a divider" style="left:363px;top:552px;height:36px"></div>
  <div class="a partner" style="left:400px;top:561px;width:90px;height:18px" role="img" aria-label="Partner badge"></div>
  <div class="a divider" style="left:525px;top:552px;height:36px"></div>
  <div class="a partner" style="left:562px;top:561px;width:100px;height:18px" role="img" aria-label="Partner badge"></div>
  <div class="a circle-btn" style="left:691px;top:558px;width:24px;height:24px"><svg width="10" height="8" viewBox="0 0 10 8"><path d="M1 4h8M6 1l3 3-3 3" stroke="#333" fill="none" stroke-width="1"/></svg></div>

  <!-- about -->
  <div class="a photo-about" style="left:47px;top:680px;width:275px;height:278px" role="img" aria-label="Photo of a hand touching a glowing cloud network"></div>
  <div class="a kicker" style="left:374px;top:682px;font-size:11px">Get To Know Us</div>
  <div class="a h2" style="left:374px;top:698px;font-size:30px">About Us</div>
  <div class="a p" style="left:374px;top:756px;width:300px;font-size:7.5px;line-height:13px">Byte Lantern is a company which intends to be in front of the client's needs, deeply understanding clients' business and delivering and optimizing solutions from the initial phase of scoping the requirements, up to the final delivery, maintenance and continuous upgrade. Byte Lantern focuses always from the customer perspective to grasp their business need for the IT solutions they deliver.</div>
  <div class="a p" style="left:374px;top:851px;width:300px;font-size:7.5px;line-height:13px">Our team operates with enthusiasm and flexibility. We are focused on our customers, being their reliable partner for services and solutions, working together on a partnership basis, helping clients with challenging problems to solve.</div>
  <div class="a btn-red" style="left:374px;top:940px;width:68px;height:20px;font-size:8px;line-height:20px">Show More</div>
  <svg class="a" style="left:448px;top:943px" width="8" height="14" viewBox="0 0 8 14"><path d="M4 1v11M1 9l3 3 3-3" stroke="#333" fill="none"/></svg>

  <!-- services band -->
  <svg class="a" style="left:0;top:960px" width="764" height="700" viewBox="0 0 764 700" aria-hidden="true">
    <path d="M0 120 C120 30 220 30 330 80 C460 140 600 90 764 20 L764 560 C650 540 560 600 460 640 C320 700 200 640 0 620 Z" fill="var(--soft)"/>
    <circle cx="700" cy="380" r="140" fill="none" stroke="rgba(238,47,58,.06)" stroke-width="14"/>
  </svg>
  <div class="a h2" style="left:95px;top:1183px;font-size:30px;line-height:36px">The Service We<br>Provide With<br>Perfection</div>
  <div class="a p" style="left:95px;top:1318px;width:222px;font-size:7.5px;line-height:13px">Lorem Ipsum is simply dummy text of the printing and typesetting industry. Lorem Ipsum has been the industry's standard dummy text ever since the 1500s, when an unknown printer took a galley of type and scrambled it to make a type specimen book.</div>

  <div class="a svc-icon" style="left:426px;top:1148px;width:48px;height:48px"><svg width="22" height="22" viewBox="0 0 22 22"><rect x="2" y="4" width="18" height="13" fill="none" stroke="#c4357a"/><path d="M5 14l4-4 3 3 5-5" stroke="#c4357a" fill="none"/></svg></div>
  <div class="a svc-title" style="left:426px;top:1220px;font-size:8.5px">Platform Architecture</div>
  <div class="a p" style="left:426px;top:1244px;width:135px;font-size:6.5px;line-height:11px">Byte Lantern works very closely with clients, product managers....</div>

  <div class="a svc-icon fill" style="left:588px;top:1148px;width:48px;height:48px"><svg width="22" height="22" viewBox="0 0 22 22"><circle cx="11" cy="11" r="4" fill="none" stroke="#fff"/><path d="M11 2v5M11 15v5M2 11h5M15 11h5" stroke="#fff"/></svg></div>
  <div class="a svc-title" style="left:588px;top:1220px;font-size:8.5px">Data Engineering</div>
  <div class="a p" style="left:588px;top:1244px;width:125px;font-size:6.5px;line-height:11px">Byte Lantern employs the latest proven technologies....</div>

  <div class="a svc-icon" style="left:426px;top:1305px;width:48px;height:48px"><svg width="22" height="22" viewBox="0 0 22 22"><path d="M6 14a4 4 0 010-8 5 5 0 019 1 3.5 3.5 0 010 7z" fill="none" stroke="#c4357a"/><path d="M11 14v5M8 19h6" stroke="#c4357a"/></svg></div>
  <div class="a svc-title" style="left:426px;top:1375px;font-size:8.5px">Cloud Developments</div>
  <div class="a p" style="left:426px;top:1398px;width:135px;font-size:6.5px;line-height:11px">Byte Lantern works very closely with clients, product managers....</div>

  <!-- team -->
  <div class="a kicker center" style="left:0;width:764px;top:1641px;font-size:11px">Company Members</div>
  <div class="a h2 center" style="left:0;width:764px;top:1657px;font-size:30px">Photos &amp; Profiles</div>
  <div class="a p center" style="left:136px;width:492px;top:1716px;font-size:7.5px;line-height:13px">Lorem Ipsum is simply dummy text of the printing and typesetting industry. Lorem Ipsum has been the industry's standard dummy text ever since the 1500s, when an unknown printer took a galley of type and scrambled</div>
  <div class="a faint-ring" style="left:60px;top:1860px;width:200px;height:200px"></div>
  <div class="a portrait" style="left:95px;top:1794px;width:240px;height:240px" role="img" aria-label="Portrait photo of the company founder"></div>
  <div class="a" style="left:379px;top:1802px;font-size:11px;font-weight:500">Theo Marsh</div>
  <div class="a" style="left:379px;top:1824px;font-size:7px;color:#c9c9c9;letter-spacing:2px">FOUNDER</div>
  <div class="a p" style="left:379px;top:1855px;width:295px;font-size:7px;line-height:11.5px">Theo manages all the client interactions and engineering team at Byte Lantern. Theo has over 15 years of experience in the technology before he founded Byte Lantern. He managed development of large scale enterprise wide, high performance, scalable, real-time software solutions in Tele-communications, Gaming, Finance, and Insurance industries.<br>He spends time working on open source projects, contributions to open-source data connectors and other projects. In free time, Theo enjoys travelling to historical places, playing sports - run, bike, tennis, ping-pong and spending time with family.</div>
  <div class="a social" style="left:379px;top:2025px;width:16px;height:16px"></div>
  <div class="a social" style="left:408px;top:2025px;width:16px;height:16px;background:#1e6fb8"></div>
  <svg class="a" style="left:589px;top:2028px" width="62" height="10" viewBox="0 0 62 10"><path d="M26 5H1M5 1L1 5l4 4M36 5h25M57 1l4 4-4 4" stroke="#333" fill="none"/></svg>

  <!-- CTA -->
  <div class="a cta" style="left:0;top:2129px;width:764px;height:176px"></div>
  <div class="a white semi" style="left:95px;top:2180px;font-size:30px;line-height:36px">Ready To Get<br>Started?</div>
  <div class="a white" style="left:362px;top:2198px;font-size:7px">Go fast and be confident in the next step on your DataOps journey.</div>
  <div class="a btn-white" style="left:362px;top:2220px;width:92px;height:20px;font-size:7.5px;line-height:20px">Request A Demo</div>

  <!-- news -->
  <div class="a kicker center" style="left:0;width:764px;top:2392px;font-size:11px">Our Latest</div>
  <div class="a h2 center" style="left:0;width:764px;top:2408px;font-size:30px">News &amp; Blogs</div>
  <div class="a p center" style="left:136px;width:492px;top:2466px;font-size:7.5px;line-height:13px">Lorem Ipsum is simply dummy text of the printing and typesetting industry. Lorem Ipsum has been the industry's standard dummy text ever since the 1500s, when an unknown printer took a galley of type and scrambled</div>

  <div class="a circle-btn" style="left:49px;top:2626px;width:28px;height:28px;border:1px solid #999;box-shadow:none"><svg width="8" height="10" viewBox="0 0 8 10"><path d="M6 1L2 5l4 4" stroke="#333" fill="none"/></svg></div>
  <div class="a card" style="left:95px;top:2545px;width:276px;height:189px">
    <div class="a card-img" style="left:183px;top:0;width:93px;height:189px" role="img" aria-label="Blog image of a glowing digital globe"></div>
    <div class="a" style="left:38px;top:36px;font-size:11px">Your Text Here</div>
    <div class="a p" style="left:38px;top:66px;width:126px;font-size:7px;line-height:12px">Lorem Ipsum is simply dummy text of the printing and typesetting industry. Lorem Ipsum has been the industry's standard dummy</div>
    <svg class="a" style="left:38px;top:150px" width="42" height="8" viewBox="0 0 42 8"><path d="M0 4h40M36 1l4 3-4 3" stroke="#ee2f3a" fill="none"/></svg>
  </div>
  <div class="a card" style="left:392px;top:2545px;width:276px;height:189px">
    <div class="a card-img desk" style="left:183px;top:0;width:93px;height:189px" role="img" aria-label="Blog image of hands typing on a laptop"></div>
    <div class="a" style="left:38px;top:36px;font-size:11px">Your Text Here</div>
    <div class="a p" style="left:38px;top:66px;width:126px;font-size:7px;line-height:12px">Lorem Ipsum is simply dummy text of the printing and typesetting industry. Lorem Ipsum has been the industry's standard dummy</div>
    <svg class="a" style="left:38px;top:150px" width="42" height="8" viewBox="0 0 42 8"><path d="M0 4h40M36 1l4 3-4 3" stroke="#ee2f3a" fill="none"/></svg>
  </div>
  <div class="a circle-btn" style="left:689px;top:2626px;width:28px;height:28px;border:1px solid #999;box-shadow:none"><svg width="8" height="10" viewBox="0 0 8 10"><path d="M2 1l4 4-4 4" stroke="#333" fill="none"/></svg></div>

  <!-- footer -->
  <div class="a footer" style="left:0;top:2822px;width:764px;height:293px"></div>
  <div class="a f-head" style="left:95px;top:2873px;font-size:11px">Quick Links</div>
  <div class="a f-link" style="left:95px;top:2917px;font-size:7px;line-height:19.5px">Home<br>Our Services<br>About Us<br>Blogs<br>Contact Us</div>
  <div class="a f-head" style="left:257px;top:2873px;font-size:11px">Others</div>
  <svg class="a" style="left:257px;top:2918px" width="10" height="8" viewBox="0 0 10 8"><rect x=".5" y=".5" width="9" height="7" fill="none" stroke="#ccc"/><path d="M.5 .5l4.5 4 4.5-4" stroke="#ccc" fill="none"/></svg>
  <div class="a f-link" style="left:278px;top:2917px;font-size:7px">info@bytelantern.com</div>
  <svg class="a" style="left:258px;top:2950px" width="9" height="12" viewBox="0 0 9 12"><path d="M4.5 11C1 6.5 1 5 1 4.5a3.5 3.5 0 017 0c0 .5 0 2-3.5 6.5z" fill="none" stroke="#ccc"/><circle cx="4.5" cy="4.5" r="1.3" fill="#ccc"/></svg>
  <div class="a f-link" style="left:278px;top:2950px;width:110px;font-size:7px;line-height:13px">18 Orchard Lane, Fairview, CA, 94010, United States</div>
  <div class="a s-dot" style="left:258px;top:3022px;width:14px;height:14px"></div>
  <div class="a s-dot" style="left:280px;top:3022px;width:14px;height:14px;background:#2b93d6"></div>
  <div class="a s-dot" style="left:302px;top:3022px;width:14px;height:14px;background:#c4357a"></div>
  <div class="a s-dot" style="left:324px;top:3022px;width:14px;height:14px;background:#1e6fb8"></div>
  <div class="a f-head" style="left:450px;top:2873px;font-size:11px">Get In Touch</div>
  <div class="a f-field" style="left:450px;top:2915px;width:220px;font-size:7px;padding-bottom:6px">Name</div>
  <div class="a f-field" style="left:450px;top:2942px;width:220px;font-size:7px;padding-bottom:6px">Email</div>
  <div class="a f-field" style="left:450px;top:2968px;width:220px;font-size:7px;padding-bottom:6px">Phone No</div>
  <div class="a f-field" style="left:450px;top:2995px;width:220px;height:70px;font-size:7px">Message</div>
  <svg class="a" style="left:652px;top:3035px" width="16" height="14" viewBox="0 0 16 14"><path d="M1 7L15 1 11 13 8 8z" fill="var(--red)"/></svg>
  <div class="a footer-bar" style="left:0;top:3115px;width:764px;height:42px"></div>
  <div class="a logo-text" style="left:95px;top:3130px;font-size:9px;color:#fff"><span class="logo-dot" style="width:7px;height:7px;margin-right:4px"></span>BYTE LANTERN</div>
  <div class="a" style="left:470px;width:200px;top:3132px;font-size:7px;color:#cfcfcf;text-align:right">Copyright © 2020, byte lantern LLC</div>
</section>

<!-- ================= MOBILE ================= -->
<section class="a frame mobile" aria-label="Mobile layout">
  <div class="a logo-text" style="left:13px;top:14px;font-size:5.5px"><span class="logo-dot" style="width:5px;height:5px;margin-right:3px"></span>BYTE LANTERN</div>
  <svg class="a" style="left:153px;top:13px" width="12" height="9" viewBox="0 0 12 9"><path d="M0 .5h12M0 4.5h12M0 8.5h12" stroke="#c4357a"/></svg>

  <div class="a hero" style="left:0;top:37px;width:178px;height:361px">
    <div class="a ring" style="left:-80px;top:-60px;width:220px;height:220px"></div>
    <div class="a ring" style="left:60px;top:140px;width:240px;height:240px"></div>
    <div class="a center white light" style="left:0;width:178px;top:72px;font-size:8px">Let's Put Your</div>
    <div class="a center white semi" style="left:0;width:178px;top:88px;font-size:15px">Data To Work</div>
    <div class="a center white" style="left:16px;width:146px;top:131px;font-size:4.5px;line-height:8.5px">Lorem Ipsum Is Simply Dummy Text Of The Printing And Typesetting Industry. Lorem Ipsum Has Been The Industry's Standard Dummy Text Ever Since The 1500s, When An Unknown Printer Took A Galley Of Type And Scrambled It To Make A Type Specimen Book</div>
    <div class="a btn-outline" style="left:60px;top:236px;width:58px;height:16px;font-size:5px;line-height:14px">Get Started</div>
  </div>

  <div class="a partner" style="left:0;top:444px;width:22px;height:10px"></div>
  <div class="a divider" style="left:48px;top:436px;height:26px"></div>
  <div class="a partner" style="left:70px;top:441px;width:38px;height:16px" role="img" aria-label="Partner badge"></div>
  <div class="a divider" style="left:132px;top:436px;height:26px"></div>
  <div class="a partner" style="left:152px;top:444px;width:30px;height:10px"></div>

  <div class="a photo-about" style="left:13px;top:505px;width:152px;height:152px;border-radius:0 0 64px 0" role="img" aria-label="Photo of a hand touching a glowing cloud network"></div>
  <div class="a kicker" style="left:13px;top:695px;font-size:6px">Get To Know Us</div>
  <div class="a h2" style="left:13px;top:708px;font-size:13px">About Us</div>
  <div class="a p" style="left:13px;top:752px;width:150px;font-size:4.5px;line-height:8.6px">Byte Lantern is a company which intends to be in front of the client's needs, deeply understanding clients' business and delivering and optimizing solutions from the initial phase of scoping the requirements, up to the final delivery, maintenance and continuous upgrade. Byte Lantern focuses always from the customer perspective to grasp their business need for the IT solutions they deliver.</div>
  <div class="a p" style="left:13px;top:880px;width:150px;font-size:4.5px;line-height:8.6px">Our team operates with enthusiasm and flexibility. We are focused on our customers, being their reliable partner for services and solutions, working together on a partnership basis, helping clients with challenging problems to solve.</div>
  <div class="a btn-red" style="left:13px;top:977px;width:58px;height:14px;font-size:4.5px;line-height:14px">Show More</div>
  <svg class="a" style="left:76px;top:978px" width="6" height="11" viewBox="0 0 6 11"><path d="M3 1v8M1 7l2 2 2-2" stroke="#333" fill="none"/></svg>

  <svg class="a" style="left:0;top:1020px" width="178" height="760" viewBox="0 0 178 760" aria-hidden="true">
    <path d="M0 30 C60 0 110 20 178 6 L178 730 C120 760 60 720 0 745 Z" fill="var(--soft)"/>
  </svg>
  <div class="a h2" style="left:13px;top:1085px;font-size:13px;line-height:16px">The Service We<br>Provide With<br>Perfection</div>
  <div class="a p" style="left:13px;top:1174px;width:140px;font-size:4.5px;line-height:8.6px">Lorem Ipsum is simply dummy text of the printing and typesetting industry. Lorem Ipsum has been the industry's standard dummy text ever since the 1500s, when an unknown printer took a galley of type and scrambled it to make a type specimen book.</div>

  <div class="a svc-icon" style="left:23px;top:1302px;width:32px;height:32px"><svg width="14" height="14" viewBox="0 0 22 22"><rect x="2" y="4" width="18" height="13" fill="none" stroke="#c4357a"/><path d="M5 14l4-4 3 3 5-5" stroke="#c4357a" fill="none"/></svg></div>
  <div class="a svc-title" style="left:13px;top:1361px;font-size:5.5px">Platform Architecture</div>
  <div class="a p" style="left:13px;top:1385px;width:150px;font-size:4.5px;line-height:8px">Byte Lantern works very closely with clients, product managers....</div>

  <div class="a svc-icon fill" style="left:23px;top:1449px;width:32px;height:32px"><svg width="14" height="14" viewBox="0 0 22 22"><circle cx="11" cy="11" r="4" fill="none" stroke="#fff"/><path d="M11 2v5M11 15v5M2 11h5M15 11h5" stroke="#fff"/></svg></div>
  <div class="a svc-title" style="left:13px;top:1508px;font-size:5.5px">Data Engineering</div>
  <div class="a p" style="left:13px;top:1532px;width:150px;font-size:4.5px;line-height:8px">Byte Lantern employs the latest proven technologies....</div>

  <div class="a svc-icon" style="left:23px;top:1598px;width:32px;height:32px"><svg width="14" height="14" viewBox="0 0 22 22"><path d="M6 14a4 4 0 010-8 5 5 0 019 1 3.5 3.5 0 010 7z" fill="none" stroke="#c4357a"/><path d="M11 14v5M8 19h6" stroke="#c4357a"/></svg></div>
  <div class="a svc-title" style="left:13px;top:1654px;font-size:5.5px">Cloud Developments</div>
  <div class="a p" style="left:13px;top:1681px;width:150px;font-size:4.5px;line-height:8px">Byte Lantern works very closely with clients, product managers....</div>

  <div class="a kicker center" style="left:0;width:178px;top:1819px;font-size:5.5px">Company Members</div>
  <div class="a h2 center" style="left:0;width:178px;top:1836px;font-size:13px">Photos &amp; Profiles</div>
  <div class="a p center" style="left:16px;width:146px;top:1874px;font-size:4.5px;line-height:8.5px">Lorem Ipsum is simply dummy text of the printing and typesetting industry. Lorem Ipsum has been the industry's standard dummy text ever since the 1500s, when an unknown printer took a galley of type and scrambled</div>
  <div class="a portrait" style="left:13px;top:1972px;width:132px;height:132px" role="img" aria-label="Portrait photo of the company founder"></div>
  <div class="a" style="left:13px;top:2141px;font-size:6px;font-weight:500">Theo Marsh</div>
  <svg class="a" style="left:124px;top:2142px" width="42" height="8" viewBox="0 0 42 8"><path d="M17 4H1M4 1L1 4l3 3M25 4h16M38 1l3 3-3 3" stroke="#333" fill="none"/></svg>
  <div class="a" style="left:13px;top:2156px;font-size:4px;color:#c9c9c9;letter-spacing:1px">FOUNDER</div>
  <div class="a p" style="left:13px;top:2181px;width:150px;font-size:4.5px;line-height:8.5px">Theo manages all the client interactions and engineering team at Byte Lantern. Theo has over 15 years of experience in the technology before he founded Byte Lantern. He managed development of large scale enterprise wide, high performance, scalable, real-time software solutions in Tele-communications, Gaming, Finance, and Insurance industries.<br>He spends time working on open source projects, contributions to open-source data connectors and other projects. In free time, Theo enjoys travelling to historical places, playing sports - run, bike, tennis, ping-pong and spending time with family.</div>
  <div class="a social" style="left:15px;top:2397px;width:13px;height:13px"></div>
  <div class="a social" style="left:43px;top:2397px;width:13px;height:13px;background:#1e6fb8"></div>

  <div class="a cta" style="left:0;top:2462px;width:178px;height:221px"></div>
  <div class="a white semi" style="left:13px;top:2494px;font-size:13px;line-height:17px">Ready To Get<br>Started?</div>
  <div class="a white" style="left:13px;top:2566px;width:155px;font-size:4.5px;line-height:8.5px">Go fast and be confident in the next step on your DataOps journey.</div>
  <div class="a btn-white" style="left:13px;top:2614px;width:81px;height:14px;font-size:4.5px;line-height:14px">Request A Demo</div>

  <div class="a kicker center" style="left:0;width:178px;top:2735px;font-size:5.5px">Our Latest</div>
  <div class="a h2 center" style="left:0;width:178px;top:2751px;font-size:13px">News &amp; Blogs</div>
  <div class="a p center" style="left:16px;width:146px;top:2790px;font-size:4.5px;line-height:8.5px">Lorem Ipsum is simply dummy text of the printing and typesetting industry. Lorem Ipsum has been the industry's standard dummy text ever since the 1500s, when an unknown printer took a galley of type and scrambled</div>
  <div class="a card" style="left:13px;top:2888px;width:152px;height:114px">
    <div class="a card-img" style="left:100px;top:0;width:52px;height:114px" role="img" aria-label="Blog image of a glowing digital globe"></div>
    <div class="a" style="left:19px;top:18px;font-size:5.5px">Your Text Here</div>
    <div class="a p" style="left:19px;top:38px;width:72px;font-size:4.5px;line-height:8px">Lorem Ipsum is simply dummy text of the printing and typesetting</div>
    <svg class="a" style="left:19px;top:89px" width="26" height="6" viewBox="0 0 26 6"><path d="M0 3h24M21 1l3 2-3 2" stroke="#ee2f3a" fill="none"/></svg>
  </div>
  <div class="a circle-btn" style="left:67px;top:3025px;width:18px;height:18px;border:1px solid #999;box-shadow:none"><svg width="5" height="7" viewBox="0 0 5 7"><path d="M4 .5L1 3.5l3 3" stroke="#333" fill="none"/></svg></div>
  <div class="a circle-btn" style="left:94px;top:3025px;width:18px;height:18px;border:1px solid #999;box-shadow:none"><svg width="5" height="7" viewBox="0 0 5 7"><path d="M1 .5l3 3-3 3" stroke="#333" fill="none"/></svg></div>

  <div class="a footer" style="left:0;top:3095px;width:178px;height:521px"></div>
  <div class="a f-head" style="left:13px;top:3138px;font-size:6.5px">Get In Touch</div>
  <div class="a f-field" style="left:13px;top:3171px;width:152px;font-size:4.5px;padding-bottom:5px">Name</div>
  <div class="a f-field" style="left:13px;top:3198px;width:152px;font-size:4.5px;padding-bottom:5px">Email</div>
  <div class="a f-field" style="left:13px;top:3226px;width:152px;font-size:4.5px;padding-bottom:5px">Phone No</div>
  <div class="a f-field" style="left:13px;top:3252px;width:152px;height:65px;font-size:4.5px">Message</div>
  <svg class="a" style="left:153px;top:3300px" width="11" height="10" viewBox="0 0 16 14"><path d="M1 7L15 1 11 13 8 8z" fill="var(--red)"/></svg>
  <div class="a f-head" style="left:13px;top:3363px;font-size:6.5px">Quick Links</div>
  <div class="a f-link" style="left:13px;top:3397px;font-size:4.5px;line-height:14px;width:160px">Home&nbsp;&nbsp;&nbsp;&nbsp;&nbsp;Our Services&nbsp;&nbsp;&nbsp;&nbsp;&nbsp;About Us<br>Blogs&nbsp;&nbsp;&nbsp;&nbsp;&nbsp;Contact Us</div>
  <div class="a f-head" style="left:13px;top:3452px;font-size:6.5px">Others</div>
  <svg class="a" style="left:14px;top:3489px" width="8" height="6" viewBox="0 0 10 8"><rect x=".5" y=".5" width="9" height="7" fill="none" stroke="#ccc"/><path d="M.5 .5l4.5 4 4.5-4" stroke="#ccc" fill="none"/></svg>
  <div class="a f-link" style="left:32px;top:3488px;font-size:4.5px">info@bytelantern.com</div>
  <svg class="a" style="left:15px;top:3514px" width="7" height="9" viewBox="0 0 9 12"><path d="M4.5 11C1 6.5 1 5 1 4.5a3.5 3.5 0 017 0c0 .5 0 2-3.5 6.5z" fill="none" stroke="#ccc"/></svg>
  <div class="a f-link" style="left:32px;top:3514px;width:130px;font-size:4.5px;line-height:8.5px">18 Orchard Lane, Fairview, CA, 94010, United States</div>
  <div class="a s-dot" style="left:15px;top:3555px;width:11px;height:11px"></div>
  <div class="a s-dot" style="left:31px;top:3555px;width:11px;height:11px;background:#2b93d6"></div>
  <div class="a s-dot" style="left:47px;top:3555px;width:11px;height:11px;background:#c4357a"></div>
  <div class="a s-dot" style="left:67px;top:3555px;width:11px;height:11px;background:#1e6fb8"></div>
  <div class="a footer-bar" style="left:0;top:3616px;width:178px;height:57px"></div>
  <div class="a logo-text center" style="left:0;width:178px;top:3630px;font-size:5.5px;color:#fff"><span class="logo-dot" style="width:5px;height:5px;margin-right:3px"></span>BYTE LANTERN</div>
  <div class="a center" style="left:0;width:178px;top:3647px;font-size:4.5px;color:#cfcfcf">Copyright © 2020, byte lantern LLC</div>
</section>

</body>
</html>
```